New Business Card Design Project

Need a design that will create an impact / strong impression towards our clients for our business. We are in the lighting business and we do lighting retrofits for large commercial to industrial clientele.

Target Market(s)

Lighting Industry

Industry/Entity Type

Business

Other font styles liked:
• we would like to use the font on our logo, not sure what it is though..

Requirements
Must have
• Our logo.
Nice to have
• We are open to suggestions that have to do with lighting.

```html
<!DOCTYPE html>
<html lang="en">
<head>
<meta charset="utf-8">
<title>Brightway Retrofit Co. – Business Card</title>
<link href="https://fonts.googleapis.com/css2?family=Montserrat:wght@400;500;600&display=swap" rel="stylesheet">
<style>
  :root {
    --backdrop: #161616;
    --card: #222222;
    --card-edge: #2a2a2a;
    --white: #f2f2f2;
    --green: #2f9e4f;
    --green-light: #6cc463;
  }
  * { box-sizing: border-box; margin: 0; padding: 0; }
  html, body {
    width: 1200px; height: 900px; overflow: hidden;
    background: var(--backdrop);
    font-family: "Montserrat", sans-serif;
    color: var(--white);
  }
  .canvas {
    position: relative; width: 1200px; height: 900px;
  }
  .card {
    position: absolute; left: 250px; width: 700px; height: 400px;
    background: linear-gradient(135deg, var(--card) 0%, var(--card-edge) 100%);
    box-shadow: 0 10px 30px rgba(0,0,0,.6);
  }
  .card--front { top: 40px; }
  .card--back { top: 460px; }

  .wordmark {
    display: flex; align-items: center; gap: 14px;
    font-weight: 600; color: var(--white);
    letter-spacing: 2px; text-transform: uppercase;
  }
  .wordmark__square {
    width: 22px; height: 22px; background: var(--green);
  }
  .wordmark__name { font-size: 34px; line-height: 1; }

  .card--front .wordmark {
    position: absolute; top: 170px; left: 0; right: 0; justify-content: center;
  }
  .card--front .web {
    position: absolute; bottom: 48px; left: 0; right: 0; text-align: center;
    font-size: 15px; letter-spacing: 2px;
  }
  .web .domain { color: var(--green-light); }

  .card--back .wordmark {
    position: absolute; top: 150px; left: 50px;
  }
  .card--back .wordmark__name { font-size: 26px; }
  .divider {
    position: absolute; left: 390px; top: 100px; width: 1.5px; height: 150px;
    background: var(--green);
  }
  .contact {
    position: absolute; left: 425px; top: 100px;
  }
  .contact__name {
    color: var(--green); font-size: 24px; font-weight: 400;
    letter-spacing: 1.5px; text-transform: uppercase;
  }
  .contact__role { font-size: 19px; margin-top: 2px; margin-bottom: 20px; }
  .contact__line {
    display: flex; align-items: center; gap: 14px;
    font-size: 15px; letter-spacing: 1px; margin-bottom: 6px;
  }
  .contact__line svg { width: 14px; height: 14px; flex: none; }
  .address {
    position: absolute; left: 0; right: 0; bottom: 48px; text-align: center;
    font-size: 17px; letter-spacing: 1.2px;
  }
</style>
</head>
<body>
<div class="canvas">
  <section class="card card--front">
    <div class="wordmark">
      <span class="wordmark__square"></span>
      <span class="wordmark__name">Brightway Retrofit Co.</span>
    </div>
    <p class="web">www.<span class="domain">brightwayretrofit</span>.com</p>
  </section>

  <section class="card card--back">
    <div class="wordmark">
      <span class="wordmark__square"></span>
      <span class="wordmark__name">Brightway<br>Retrofit Co.</span>
    </div>
    <div class="divider"></div>
    <div class="contact">
      <p class="contact__name">Daniel Hart</p>
      <p class="contact__role">Founder</p>
      <p class="contact__line">
        <svg viewBox="0 0 24 24" fill="var(--green)"><path d="M6.6 10.8a15 15 0 0 0 6.6 6.6l2.2-2.2a1 1 0 0 1 1-.25 11.4 11.4 0 0 0 3.6.57 1 1 0 0 1 1 1V20a1 1 0 0 1-1 1A17 17 0 0 1 3 4a1 1 0 0 1 1-1h3.5a1 1 0 0 1 1 1c0 1.25.2 2.45.57 3.6a1 1 0 0 1-.25 1z"/></svg>
        0400 555 019
      </p>
      <p class="contact__line">
        <svg viewBox="0 0 24 24" fill="var(--green)"><path d="M2 5h20v14H2z" opacity=".9"/><path d="M2 5l10 8 10-8" fill="none" stroke="#222" stroke-width="2"/></svg>
        info@brightwayretrofit.com
      </p>
      <p class="contact__line">
        <svg viewBox="0 0 24 24" fill="none" stroke="var(--green)" stroke-width="2"><circle cx="12" cy="12" r="9"/><path d="M3 12h18M12 3c3 3 3 15 0 18M12 3c-3 3-3 15 0 18"/></svg>
        www.brightwayretrofit.com
      </p>
    </div>
    <p class="address">4820 West Harbor Lane, Suite C204 Mesa AZ 85201</p>
  </section>
</div>
</body>
</html>
```